business card & stationary
bus.card
business card & stationary -
Creative Brief
Corporate
Rodrigo Valcárcel
Chairman of the Board
2237 West Pelham Corvel Bay, Oregon 79413
rvalcarcel@valcarcelgroup.example
qbnl.example

```html
<!DOCTYPE html>
<html lang="en">
<head>
<meta charset="utf-8">
<title>Meridian Lending Group – Business Card</title>
<link rel="stylesheet" href="https://fonts.googleapis.com/css2?family=Noto+Serif:ital,wght@0,400;0,700;1,400&display=swap">
<style>
  :root {
    --bg: #e9e6e1;
    --card: #ffffff;
    --green: #1f8a3c;
    --green-dark: #146b2c;
    --green-light: #4fb35e;
    --gold: #b08a3e;
    --ink: #4a4a4a;
    --rule: #d4cfc4;
  }
  * { box-sizing: border-box; margin: 0; padding: 0; }
  html, body { width: 1200px; height: 646px; overflow: hidden; }
  body {
    background: var(--bg);
    font-family: "Noto Serif", serif;
    color: var(--ink);
    position: relative;
  }
  .card {
    position: absolute;
    top: 174px;
    width: 520px;
    height: 298px;
    background: var(--card);
    box-shadow: 0 6px 18px rgba(0,0,0,.18);
    overflow: hidden;
  }
  .card--back { left: 50px; }
  .card--front { left: 630px; }

  .brand {
    color: var(--green);
    font-weight: 700;
    text-align: center;
    letter-spacing: 1px;
    line-height: 1.15;
  }
  .card--back .brand {
    position: absolute;
    left: 0; right: 0; top: 108px;
    font-size: 30px;
  }
  .card--back .url {
    position: absolute;
    left: 26px; bottom: 24px;
    font-size: 11px;
    line-height: 1.2;
    color: var(--ink);
  }

  .card--front .brand-area {
    position: absolute;
    left: 0; top: 0; width: 250px; height: 250px;
    display: flex; align-items: center; justify-content: center;
  }
  .card--front .brand { font-size: 24px; }
  .divider {
    position: absolute;
    left: 252px; top: 28px;
    width: 1px; height: 200px;
    background: var(--rule);
  }
  .details {
    position: absolute;
    left: 274px; top: 30px; right: 20px;
    font-size: 11px;
    line-height: 1.5;
  }
  .details .name { color: var(--green); font-weight: 700; font-size: 17px; line-height: 1.2; }
  .details .title { color: var(--gold); font-style: italic; font-size: 12px; margin-bottom: 14px; }
  .details .address { margin-bottom: 14px; }
  .contact { list-style: none; }
  .contact li { display: flex; align-items: center; gap: 7px; margin-bottom: 3px; white-space: nowrap; }
  .contact svg { width: 13px; height: 13px; flex: none; }

  .band {
    position: absolute;
    left: 0; right: 0; bottom: 0; height: 28px;
    background: linear-gradient(90deg, var(--green-dark), var(--green-light));
    border-top: 3px solid var(--gold);
  }
</style>
</head>
<body>
  <section class="card card--back">
    <div class="brand">Meridian<br>Lending Group, LLC</div>
    <div class="url">www.qbnl.example</div>
  </section>

  <section class="card card--front">
    <div class="brand-area">
      <div class="brand">Meridian<br>Lending Group, LLC</div>
    </div>
    <div class="divider"></div>
    <div class="details">
      <div class="name">Rodrigo Valcárcel</div>
      <div class="title">Chairman of the Board</div>
      <div class="address">2237 West Pelham<br>Corvel Bay, Oregon 79413</div>
      <ul class="contact">
        <li><svg viewBox="0 0 16 16"><circle cx="8" cy="8" r="8" fill="#1f8a3c"/><path d="M5 4h2l1 2-1 1a5 5 0 0 0 2 2l1-1 2 1v2c-4 0-7-3-7-7z" fill="#fff"/></svg>555-210-0142</li>
        <li><svg viewBox="0 0 16 16"><circle cx="8" cy="8" r="8" fill="#1f8a3c"/><path d="M5 4h2l1 2-1 1a5 5 0 0 0 2 2l1-1 2 1v2c-4 0-7-3-7-7z" fill="#fff"/></svg>555-210-0178</li>
        <li><svg viewBox="0 0 16 16"><circle cx="8" cy="8" r="8" fill="#1f8a3c"/><path d="M5 4h2l1 2-1 1a5 5 0 0 0 2 2l1-1 2 1v2c-4 0-7-3-7-7z" fill="#fff"/></svg>555-210-0193</li>
        <li><svg viewBox="0 0 16 16"><circle cx="8" cy="8" r="8" fill="#1f8a3c"/><rect x="4" y="5" width="8" height="6" fill="#fff"/><path d="M4 5l4 3 4-3" stroke="#1f8a3c" fill="none"/></svg>rvalcarcel@valcarcelgroup.example</li>
        <li><svg viewBox="0 0 16 16"><circle cx="8" cy="8" r="8" fill="#1f8a3c"/><circle cx="8" cy="8" r="4" fill="none" stroke="#fff"/><path d="M4 8h8M8 4v8" stroke="#fff"/></svg>www.qbnl.example</li>
      </ul>
    </div>
    <div class="band"></div>
  </section>
</body>
</html>
```